TalkBridge - Language Coaching Services

Sleek, innovative, trendy design for Language Coaching business.

TalkBridge is a new UK based company that provides Language Coaching services. We offer highly personalized on-line and face to face language courses. We also impart learning techniques workshops based on the latest neuroscience research for second-language acquisition.

Target Market(s)

Industry/Entity Type

Consulting

Contact Information for Business Card

TalkBridge
ElenaVT@talkbridge-demo.co.uk
TalkBridge-demo.co.uk
London, UK

Font styles to use
Sans Serif

```html
<!DOCTYPE html>
<html lang="en">
<head>
<meta charset="utf-8">
<title>TalkBridge – Business Card</title>
<link href="https://fonts.googleapis.com/css2?family=Lexend:wght@400;500;600&display=swap" rel="stylesheet">
<style>
  :root {
    --backdrop: #efefef;
    --card-navy: #034d74;
    --mark-blue: #0d7fae;
    --card-white: #ffffff;
    --mark-pale: #dcdcdc;
    --ink-navy: #0a4d75;
  }
  * { margin: 0; padding: 0; box-sizing: border-box; }
  html, body {
    width: 1200px;
    height: 1013px;
    overflow: hidden;
    background: var(--backdrop);
    font-family: "Lexend", "Helvetica Neue", Arial, sans-serif;
  }
  .card {
    position: absolute;
    top: 133px;
    width: 471px;
    height: 729px;
  }
  .card--front { left: 84px; background: var(--card-navy); }
  .card--back  { left: 625px; background: var(--card-white); }

  .brand {
    position: absolute;
    top: 78px;
    left: 0;
    width: 100%;
    display: flex;
    flex-direction: column;
    align-items: center;
  }
  .brand__circle {
    width: 110px;
    height: 110px;
    border-radius: 50%;
  }
  .brand__name {
    margin-top: 20px;
    font-size: 40px;
    font-weight: 500;
    letter-spacing: 1px;
    text-transform: uppercase;
    line-height: 1;
  }
  .card--front .brand__circle { background: var(--mark-blue); }
  .card--front .brand__name   { color: var(--mark-blue); }
  .card--back  .brand__circle { background: var(--mark-pale); }
  .card--back  .brand__name   { color: var(--mark-pale); }

  .contact {
    position: absolute;
    top: 466px;
    left: 0;
    width: 100%;
    text-align: center;
    color: var(--ink-navy);
  }
  .contact__company {
    font-size: 26px;
    font-weight: 600;
    letter-spacing: 10px;
    text-transform: uppercase;
    padding-left: 10px;
    line-height: 1;
  }
  .contact__dot {
    width: 11px;
    height: 11px;
    border-radius: 50%;
    background: var(--ink-navy);
    margin: 22px auto 22px;
  }
  .contact__line {
    font-size: 22px;
    font-weight: 400;
    line-height: 37px;
    letter-spacing: 0.5px;
  }
</style>
</head>
<body>
  <section class="card card--front">
    <div class="brand">
      <div class="brand__circle"></div>
      <div class="brand__name">TalkBridge</div>
    </div>
  </section>

  <section class="card card--back">
    <div class="brand">
      <div class="brand__circle"></div>
      <div class="brand__name">TalkBridge</div>
    </div>
    <div class="contact">
      <div class="contact__company">TalkBridge</div>
      <div class="contact__dot"></div>
      <div class="contact__line">ElenaVT@talkbridge-demo.co.uk</div>
      <div class="contact__line">TalkBridge-demo.co.uk</div>
      <div class="contact__line">London, UK</div>
    </div>
  </section>
</body>
</html>
```